Fahrzeugbeschriftung für ein Unternehmen der Heizungsbaubranche
Zielgruppe
Wir sind ein Unternehmen der Heizungsbaubranche, Heizung, Sanitär, unsere Zielgruppe ist regional ca. 50 km Umkreis deshalb ist eine atraktive Fahrzeuggestaltung wichtig, Wir fahren Transporter wie z.B. KL Karossa R4 und Brelan Voyo Extra , außerdem PKW wie z.B. KL Piven Kombi und KL ZO, alle Fahrzeuge sind weiß.
Aufgabenstellung
Der Phantasie freien Lauf lassen !!!!
Die Fahrzeuge sollen von allen 4 Seiten beschriftet werden
Die Schrift habe ich den Dateien beigefügt.

```html
<!DOCTYPE html>
<html lang="de">
<head>
<meta charset="utf-8">
<title>Felkon Wärmetechnik – Fahrzeugbeschriftung</title>
<link rel="stylesheet" href="https://fonts.googleapis.com/css2?family=Exo+2:wght@300;400&family=Source+Sans+3:wght@300;400;600&display=swap">
<style>
  :root {
    --bg: #f1f1f1;
    --brand-blue: #4a78a6;
    --text-grey: #555a5e;
    --phone-grey: #7a7d80;
    --band-deep: #de6a1c;
    --band-mid: #eea33a;
    --band-light: #f6cf73;
    --band-gold: #e2ae2a;
  }
  * { margin: 0; padding: 0; box-sizing: border-box; }
  html, body { width: 1200px; height: 800px; overflow: hidden; }
  body {
    position: relative;
    background: var(--bg);
    font-family: "Source Sans 3", sans-serif;
  }
  .phone-line {
    position: absolute;
    left: 465px; top: 258px;
    font-family: "Source Sans 3", sans-serif;
    font-weight: 300;
    font-size: 21px;
    letter-spacing: 0.3px;
    color: var(--phone-grey);
    white-space: nowrap;
  }
  .brand {
    position: absolute;
    left: 500px; top: 350px;
    width: 320px;
    display: flex;
    align-items: center;
    gap: 10px;
  }
  .brand-dot {
    width: 22px; height: 22px;
    border-radius: 50%;
    background: var(--band-mid);
    flex: none;
  }
  .brand-name {
    font-family: "Exo 2", sans-serif;
    font-weight: 400;
    font-size: 27px;
    color: var(--brand-blue);
    white-space: nowrap;
  }
  .tagline {
    position: absolute;
    left: 523px; top: 438px;
    font-family: "Exo 2", sans-serif;
    font-weight: 300;
    font-size: 25px;
    color: var(--text-grey);
    white-space: nowrap;
  }
  .stripe {
    position: absolute;
    left: 0; top: 0;
    width: 1200px; height: 800px;
  }
  .services {
    position: absolute;
    left: 453px; top: 495px;
    display: flex;
    gap: 10px;
    list-style: none;
    font-family: "Source Sans 3", sans-serif;
    font-size: 19.5px;
    color: var(--text-grey);
    white-space: nowrap;
  }
  .services li::before {
    content: "•";
    margin-right: 1px;
  }
</style>
</head>
<body>
  <p class="phone-line">Melden Sie sich! : 069 / 58 20 91</p>

  <div class="brand">
    <span class="brand-dot"></span>
    <span class="brand-name">Felkon Wärmetechnik GmbH</span>
  </div>

  <p class="tagline">Qualität aus Meisterhand!</p>

  <svg class="stripe" viewBox="0 0 1200 800" aria-hidden="true">
    <defs>
      <linearGradient id="bandFill" x1="0" y1="0" x2="1" y2="0">
        <stop offset="0" stop-color="var(--band-deep)"/>
        <stop offset="0.45" stop-color="var(--band-mid)"/>
        <stop offset="1" stop-color="var(--band-gold)"/>
      </linearGradient>
      <linearGradient id="bandHighlight" x1="0" y1="0" x2="1" y2="0">
        <stop offset="0" stop-color="var(--band-deep)"/>
        <stop offset="1" stop-color="var(--band-light)"/>
      </linearGradient>
    </defs>
    <polygon class="band-body" points="227,527 492,485 974,485 974,527" fill="url(#bandFill)"/>
    <polygon class="band-edge" points="430,490 492,480 974,480 974,492 492,492" fill="url(#bandHighlight)" opacity="0.85"/>
  </svg>

  <ul class="services">
    <li>Sanitär</li>
    <li>Heizung</li>
    <li>Notdienst</li>
    <li>Solartechnik</li>
  </ul>
</body>
</html>
```